Stationery Required - Own Logo provided

Hi,

We are a retail company called 'Copperfinch Trading Limited' based in the UK and would like some corporate stationery designed.

We have provided our Logo which we would like to use (Its attached to this brief)...

The designs must be orginal, professional, stylish and interesting!

Target Market(s)

We will use this stationery to communicate with our wholesale suppliers and employees, so it must have a 'professional' feel about it.

Industry/Entity Type

It Company

Requirements
Must have
• Must be professional, corporate, stylish and not to 'fussy'. we require ... Business card design, a4 letter, compliment slip. All designs must be supplied in a format where the text (address/telephone numbers etc..) can be edited, as we have alot of staff and operate out of several different premises.
Nice to have
• I would like a windows backround picture file supplied as well so we can integrate that onto our computer systems.

```html
<!DOCTYPE html>
<html lang="en">
<head>
<meta charset="utf-8">
<title>Copperfinch Trading Limited – Stationery</title>
<link rel="stylesheet" href="https://fonts.googleapis.com/css2?family=Montserrat:wght@400;600;700&display=swap">
<style>
  :root{
    --lime:#8dc21f;
    --lime-light:#a6d33a;
    --forest:#3f6d12;
    --paper:#f1f1ea;
    --ink:#3a3a3a;
    --muted:#7a7a72;
    --backdrop:#dcdcd4;
  }
  *{box-sizing:border-box;margin:0;padding:0}
  html,body{width:1200px;height:1200px;overflow:hidden}
  body{background:var(--backdrop);font-family:"Montserrat",Arial,sans-serif;color:var(--ink);position:relative}
  .sheet{position:absolute;background:var(--paper);overflow:hidden;box-shadow:0 6px 18px rgba(0,0,0,.18)}
  .sheet svg.art{position:absolute;inset:0;width:100%;height:100%}
  .wordmark{position:absolute;display:flex;align-items:center;gap:7px;font-weight:700;color:var(--forest);white-space:nowrap}
  .wordmark .mark{display:inline-block;background:var(--lime)}
  .address{position:absolute;color:#fff;font-size:8px;line-height:1.45;text-align:right}
  .address strong{font-weight:700;font-size:9px;display:block}

  /* Letterhead */
  .letterhead{left:60px;top:150px;width:480px;height:680px}
  .letterhead .wordmark{left:34px;top:130px;font-size:15px}
  .letterhead .wordmark .mark{width:12px;height:12px}
  .letterhead .address{right:26px;top:12px}
  .letterhead .web{position:absolute;right:22px;bottom:6px;font-size:8px;color:#fff}

  /* Compliment slip */
  .slip{left:580px;top:150px;width:560px;height:264px}
  .slip .wordmark{left:30px;top:60px;font-size:17px}
  .slip .wordmark .mark{width:13px;height:13px}
  .slip .title{position:absolute;left:250px;top:30px;font-size:22px;font-weight:700;color:var(--forest)}
  .slip .address{right:24px;bottom:22px;font-size:9px}

  /* Envelope */
  .envelope{left:580px;top:440px;width:560px;height:280px}
  .envelope .wordmark{left:34px;bottom:34px;font-size:16px}
  .envelope .wordmark .mark{width:12px;height:12px}
  .envelope .address{right:24px;top:18px}

  /* Business cards */
  .card{top:746px;width:272px;height:176px;border-radius:10px}
  .card-front{left:580px}
  .card-back{left:868px}
  .card-front .wordmark{left:18px;top:16px;font-size:13px}
  .card-front .wordmark .mark{width:10px;height:10px}
  .card-front .person{position:absolute;left:18px;top:56px}
  .person .name{font-size:14px;font-weight:700;color:var(--forest)}
  .person .role{font-size:8px;color:var(--muted);margin-top:3px}
  .person .lines{font-size:7.5px;color:var(--muted);line-height:1.55;margin-top:6px}
  .card-front .address{right:14px;bottom:12px;font-size:7px}
  .card-back .wordmark{left:40px;top:78px;font-size:14px;color:#fff}
  .card-back .wordmark .mark{width:11px;height:11px;background:#fff}
  .card-back .web{position:absolute;right:10px;top:10px;font-size:6.5px;color:#fff}
</style>
</head>
<body>

<section class="sheet letterhead" aria-label="A4 letterhead">
  <svg class="art" viewBox="0 0 480 680" preserveAspectRatio="none">
    <path d="M0 112 C140 70 300 66 480 66 L480 0 L0 0Z" fill="var(--lime)"/>
    <path d="M0 112 C140 70 300 66 480 66" fill="none" stroke="var(--forest)" stroke-width="4"/>
    <rect x="0" y="660" width="480" height="20" fill="var(--lime)"/>
    <rect x="0" y="655" width="480" height="4" fill="var(--forest)"/>
  </svg>
  <div class="wordmark"><span class="mark"></span>Copperfinch Trading Limited</div>
  <div class="address"><strong>Copperfinch Trading Limited</strong>14 Mill Lane, Leeds LS1 4AB<br>Tel 0113 496 0321</div>
  <div class="web">www.copperfinchtrading.co.uk</div>
</section>

<section class="sheet slip" aria-label="Compliment slip">
  <svg class="art" viewBox="0 0 560 264" preserveAspectRatio="none">
    <path d="M0 264 C200 250 360 170 560 70 L560 264Z" fill="var(--lime)"/>
    <path d="M0 264 C200 250 360 170 560 70" fill="none" stroke="var(--forest)" stroke-width="5"/>
    <rect x="0" y="256" width="560" height="8" fill="var(--lime)"/>
  </svg>
  <div class="title">With Compliments</div>
  <div class="wordmark"><span class="mark"></span>Copperfinch Trading Limited</div>
  <div class="address"><strong>Copperfinch Trading Limited</strong>14 Mill Lane, Leeds LS1 4AB<br>Tel 0113 496 0321</div>
</section>

<section class="sheet envelope" aria-label="DL envelope">
  <svg class="art" viewBox="0 0 560 280" preserveAspectRatio="none">
    <path d="M0 210 C80 170 110 90 130 0 L0 0Z" fill="var(--lime)"/>
    <path d="M0 210 C80 170 110 90 130 0" fill="none" stroke="var(--forest)" stroke-width="4"/>
    <rect x="0" y="272" width="560" height="8" fill="var(--lime)"/>
    <rect x="0" y="268" width="560" height="3" fill="var(--forest)"/>
  </svg>
  <div class="wordmark"><span class="mark"></span>Copperfinch Trading Limited</div>
  <div class="address" style="color:var(--muted)"><strong style="color:var(--forest)">Copperfinch Trading Limited</strong>14 Mill Lane, Leeds LS1 4AB<br>Tel 0113 496 0321</div>
</section>

<section class="sheet card card-front" aria-label="Business card front">
  <svg class="art" viewBox="0 0 272 176" preserveAspectRatio="none">
    <path d="M0 176 C120 174 210 130 272 60 L272 176Z" fill="var(--lime)"/>
    <path d="M0 176 C120 174 210 130 272 60" fill="none" stroke="var(--forest)" stroke-width="4"/>
  </svg>
  <div class="wordmark"><span class="mark"></span>Copperfinch Trading</div>
  <div class="person">
    <div class="name">Martin Hale</div>
    <div class="role">Company Director</div>
    <div class="lines">07700 900461<br>Email: hello@copperfinchtrading.co.uk</div>
  </div>
  <div class="address">Office 0113 496 0321<br>14 Mill Lane, Leeds</div>
</section>

<section class="sheet card card-back" aria-label="Business card back">
  <svg class="art" viewBox="0 0 272 176" preserveAspectRatio="none">
    <rect width="272" height="176" fill="var(--lime)"/>
    <path d="M150 0 C210 60 215 120 190 176 L272 176 L272 0Z" fill="var(--forest)"/>
    <path d="M150 0 C210 60 215 120 190 176" fill="none" stroke="var(--paper)" stroke-width="5"/>
  </svg>
  <div class="web">www.copperfinchtrading.co.uk</div>
  <div class="wordmark"><span class="mark"></span>Copperfinch</div>
</section>

</body>
</html>
```